ValeHerb.com Cooking Spice Jar Label Design

I need the following labels designed.

dimensions in inches. Drawings attached and logo attached

a. 3.5 oz wrap around spice label 2.3" tall x 3.3" wide
b. 5.5 oz warp around spice label 3.3" tall x 3.6" wide
c. 32 oz clear bottle. Flat label
c. flat label. 2.25 x 4
d. flat front of bottle label 5 x 3.5

Target Market(s)

gourmet cooks. restaurant managers. chefs. grocery store owners.

Industry/Entity Type

Cooking

Font styles to use
Other font styles liked:
• see attached logo

Requirements
Must have
• must be elegant and sophisticated using the existing logo attached.
• please look at www.valeherb.com to see what the 3.5 oz label looks like today with the old logo.
Nice to have

```html
<!DOCTYPE html>
<html lang="en">
<head>
<meta charset="utf-8">
<title>ValeHerb Aleppo Pepper Label</title>
<link href="https://fonts.googleapis.com/css2?family=Josefin+Sans:wght@300;400;600&display=swap" rel="stylesheet">
<style>
  :root {
    --green: #8cc63f;
    --olive: #6b8a2e;
    --amber: #f7a51c;
    --orange: #f26a2e;
    --red: #b8282a;
    --ink: #3a3a3a;
    --body: #4a4a4a;
    --panel-light: #f7f8f9;
    --panel-dark: #c9cbce;
    --brand-dark: #8a2a24;
  }
  html, body { margin: 0; padding: 0; overflow: hidden; background: #fff; }
  .label {
    position: relative; width: 1200px; height: 753px; overflow: hidden;
    background: #fff; font-family: "Josefin Sans", sans-serif; color: var(--body);
  }
  .top-band {
    position: absolute; left: 18px; top: 18px; width: 1164px; height: 9px;
    background: linear-gradient(90deg, var(--red), var(--orange) 50%, var(--red));
  }
  .top-line {
    position: absolute; left: 18px; top: 27px; width: 1164px; height: 3px;
    background: linear-gradient(90deg, var(--olive), var(--amber));
  }
  .panel { position: absolute; top: 30px; height: 703px; }
  .panel--info { background: linear-gradient(90deg, var(--panel-light) 0%, #e4e6e8 60%, var(--panel-dark) 100%); }
  .panel--front { background: #fff; }
  .p1 { left: 18px; width: 245px; }
  .p2 { left: 263px; width: 337px; }
  .p3 { left: 600px; width: 246px; }
  .p4 { left: 846px; width: 336px; }

  .info-block { position: absolute; left: 18px; width: 245px; text-align: center; }
  .info-title {
    margin: 0 0 10px; font-size: 14px; font-weight: 400; color: var(--green);
    letter-spacing: 0.3px; text-transform: uppercase;
  }
  .info-text { margin: 0; font-size: 12.5px; font-weight: 300; line-height: 18px; }
  .phone { display: inline-block; vertical-align: -2px; margin-right: 8px; }

  .usage { position: absolute; left: 630px; top: 60px; width: 210px; }
  .usage .info-title { text-align: center; width: 200px; }
  .usage .info-text { text-align: left; }

  .brand {
    position: absolute; width: 337px; text-align: center; top: 124px;
    font-size: 46px; font-weight: 400; color: var(--ink); letter-spacing: 1px;
  }
  .brand-dot { display: inline-block; width: 14px; height: 14px; border-radius: 50%; background: var(--orange); vertical-align: 18px; margin-right: 8px; }
  .b2 { left: 263px; }
  .b4 { left: 846px; }

  .net { position: absolute; font-size: 11px; font-weight: 600; color: #222; }
  .n2 { left: 468px; top: 610px; }
  .n4 { left: 1063px; top: 543px; }

  .wave { position: absolute; left: 0; top: 0; }
  .product {
    position: absolute; top: 676px; font-size: 27px; font-weight: 300; color: #fff;
    width: 300px; text-align: center;
  }
  .pr2 { left: 284px; }
  .pr4 { left: 867px; }
  .mini-brand {
    position: absolute; top: 683px; width: 160px; text-align: center;
    font-size: 17px; font-weight: 400; color: var(--brand-dark);
  }
  .mb1 { left: 62px; }
  .mb3 { left: 638px; }
</style>
</head>
<body>
<div class="label">
  <div class="top-band"></div>
  <div class="top-line"></div>

  <div class="panel panel--info p1"></div>
  <div class="panel panel--front p2"></div>
  <div class="panel panel--info p3"></div>
  <div class="panel panel--front p4"></div>

  <section class="info-block" style="top:58px">
    <h2 class="info-title">Ingredients</h2>
    <p class="info-text">Place to add any description<br>of the product.</p>
  </section>
  <section class="info-block" style="top:157px">
    <h2 class="info-title">Cautions</h2>
    <p class="info-text">Place to add any other description<br>of the product.</p>
  </section>
  <section class="info-block" style="top:270px">
    <h2 class="info-title">Manufactured by</h2>
    <p class="info-text">Place to add company detail<br>Name, address of company.</p>
  </section>
  <section class="info-block" style="top:401px">
    <h2 class="info-title"><svg class="phone" width="18" height="16" viewBox="0 0 24 24"><path fill="#8cc63f" d="M6.6 10.8c1.4 2.8 3.8 5.1 6.6 6.6l2.2-2.2c.3-.3.7-.4 1-.2 1.1.4 2.3.6 3.6.6.6 0 1 .4 1 1V20c0 .6-.4 1-1 1C10.6 21 3 13.4 3 4c0-.6.4-1 1-1h3.5c.6 0 1 .4 1 1 0 1.3.2 2.5.6 3.6.1.3 0 .7-.2 1l-2.3 2.2z"/></svg>Customer Care</h2>
    <p class="info-text">Place to add company detail<br>Name, address of company.</p>
  </section>

  <section class="usage">
    <h2 class="info-title">Usage Instruction</h2>
    <p class="info-text">Place to add how to use the product:<br>1. Step one - This is step one how to use<br>the product.<br>2. Step two- This is second step how<br>to use the product.<br>3. Step three- This is third step how<br>to use the product.</p>
  </section>

  <div class="brand b2"><span class="brand-dot"></span>VALEHERB</div>
  <div class="brand b4"><span class="brand-dot"></span>VALEHERB</div>

  <div class="net n2">Netto 120 gram</div>
  <div class="net n4">Netto 120 gram</div>

  <svg class="wave" width="1200" height="753" viewBox="0 0 1200 753" aria-hidden="true">
    <defs>
      <linearGradient id="waveFill" x1="0" y1="0" x2="1" y2="0">
        <stop offset="0" stop-color="#b8282a"/>
        <stop offset="0.2" stop-color="#e0512b"/>
        <stop offset="0.5" stop-color="#f26a2e"/>
        <stop offset="0.8" stop-color="#e45a2c"/>
        <stop offset="1" stop-color="#b8282a"/>
      </linearGradient>
    </defs>
    <path d="M18 590 C300 610 450 655 650 652 C850 650 1000 590 1182 576 L1182 733 L18 733 Z" fill="#6b8a2e"/>
    <path d="M18 598 C300 618 450 662 650 659 C850 657 1000 598 1182 584 L1182 733 L18 733 Z" fill="#f7a51c"/>
    <path d="M18 604 C300 624 450 668 650 665 C850 663 1000 604 1182 590 L1182 733 L18 733 Z" fill="url(#waveFill)"/>
  </svg>

  <div class="mini-brand mb1">VALEHERB</div>
  <div class="mini-brand mb3">VALEHERB</div>
  <div class="product pr2">Aleppo Pepper</div>
  <div class="product pr4">Aleppo Pepper</div>
</div>
</body>
</html>
```